Corvane Project Services - Flyer

Project Breif:
I need a single page A4 Capability Statement, which will be used to market our services to prospective clients, both in print and via email PDF.
It needs to look professional and should incorporate the elements I have uploaded into files, these include:
Capability Statement Text
Corvane Services Company Logo
Additional Logo’s (Tools We Use)
Glimmer Bay Pics can be cut into the page
I have included examples of capability statements as a guide to what i am looking for.
Regards
Derek
Engineering Consulting

```html
<!DOCTYPE html>
<html lang="en">
<head>
<meta charset="utf-8">
<title>Corvane Project Services – Capability Statement</title>
<link rel="stylesheet" href="https://fonts.googleapis.com/css2?family=Quicksand:wght@400;500;600&family=Nunito:wght@700;800&display=swap">
<style>
  :root {
    --page-bg: #e4e6e9;
    --paper: #ffffff;
    --navy: #0d4f9c;
    --navy-deep: #0a3f80;
    --sky: #6cc0ec;
    --col-plan: #7fc7e9;
    --col-risk: #8fb1df;
    --col-cost: #86d0ef;
    --col-head-plan: #a9dcf3;
    --col-head-risk: #b4cbeb;
    --col-head-cost: #b0e1f5;
    --text-blue: #1d5fae;
    --list-blue: #2a62b0;
  }
  * { box-sizing: border-box; margin: 0; padding: 0; }
  html, body { width: 1200px; height: 900px; overflow: hidden; }
  body {
    background: var(--page-bg);
    font-family: "Quicksand", "Century Gothic", sans-serif;
    position: relative;
  }
  .flyer {
    position: absolute;
    left: 50%; top: 50%;
    width: 528px; height: 736px;
    margin-left: -264px; margin-top: -368px;
    transform: scale(1.15);
    background: var(--paper);
    box-shadow: 0 4px 18px rgba(0,0,0,.18);
  }
  /* header */
  .brand {
    position: absolute; left: 12px; top: 12px; width: 160px; height: 91px;
    display: flex; flex-direction: column; align-items: center; justify-content: flex-end;
    padding-bottom: 6px;
  }
  .brand-dot { width: 36px; height: 36px; border-radius: 50%; background: var(--navy); margin-bottom: 10px; }
  .brand-name {
    font-family: "Nunito", sans-serif; font-weight: 800; color: var(--navy-deep);
    font-size: 10.5px; letter-spacing: .6px; text-align: center; line-height: 1.15;
  }
  .header-band { position: absolute; left: 12px; top: 12px; width: 504px; height: 91px; }
  .director {
    position: absolute; right: 22px; top: 20px; text-align: right; color: #fff; z-index: 2;
  }
  .director-name {
    font-family: "Nunito", sans-serif; font-weight: 700; font-size: 20px; line-height: 20px;
    padding-bottom: 3px; border-bottom: 1px solid var(--sky); padding-left: 16px;
  }
  .director-name .first { color: var(--sky); }
  .director-role { font-size: 10px; line-height: 12px; margin-top: 1px; }
  .contacts { list-style: none; margin-top: 6px; font-size: 7.5px; line-height: 12.5px; }
  .contacts li { display: flex; justify-content: flex-end; align-items: center; gap: 3px; }
  .contacts svg { width: 8px; height: 8px; }
  /* photo */
  .hero {
    position: absolute; left: 12px; top: 103px; width: 504px; height: 250px;
    background: linear-gradient(135deg, #dfe9f2 0%, #f6f8fb 40%, #cfdde9 70%, #e9eef4 100%);
  }
  .hero-label {
    position: absolute; left: 0; bottom: 0; background: var(--navy); color: #fff;
    font-family: "Nunito", sans-serif; font-weight: 700; font-size: 13px;
    padding: 4px 8px 4px 12px;
  }
  /* intro */
  .intro {
    position: absolute; left: 24px; top: 359px; width: 484px;
    color: var(--text-blue); font-size: 9.6px; line-height: 12.8px;
  }
  .intro p + p { margin-top: 12.8px; }
  /* services */
  .services-title {
    position: absolute; left: 24px; top: 504px; background: var(--navy); color: #fff;
    font-family: "Nunito", sans-serif; font-weight: 700; font-size: 14px; padding: 1px 12px 2px 4px;
  }
  .services-rule { position: absolute; left: 24px; top: 530px; width: 481px; height: 2px; background: var(--navy); }
  .services { position: absolute; left: 24px; top: 537px; display: flex; gap: 5px; height: 136px; }
  .service { height: 100%; border-bottom: 3px solid var(--navy); }
  .service h3 {
    font-family: "Nunito", sans-serif; font-weight: 700; font-size: 11px; color: var(--navy-deep);
    padding: 1px 3px; margin-bottom: 1px;
  }
  .service ul { list-style: none; font-size: 7.6px; color: var(--list-blue); padding: 0 4px; }
  .service li { line-height: 16px; white-space: nowrap; }
  .service li::before { content: ""; display: inline-block; width: 4px; height: 4px; background: var(--navy); margin-right: 4px; vertical-align: 1px; }
  .service.plan { width: 178px; background: var(--col-plan); }
  .service.plan h3 { background: var(--col-head-plan); }
  .service.risk { width: 178px; background: var(--col-risk); }
  .service.risk h3 { background: var(--col-head-risk); }
  .service.cost { width: 115px; background: var(--col-cost); }
  .service.cost h3 { background: var(--col-head-cost); }
  /* tools */
  .tools {
    position: absolute; left: 24px; top: 692px; width: 481px;
    display: flex; justify-content: space-between; align-items: center;
  }
  .tool {
    font-family: "Quicksand", sans-serif; font-weight: 600; font-size: 9.5px; color: var(--navy-deep);
    display: flex; align-items: center; gap: 3px;
  }
  .tool i { display: inline-block; width: 8px; height: 8px; background: var(--navy); }
  .footer-bar { position: absolute; left: 24px; top: 720px; width: 481px; height: 4px; display: flex; }
  .footer-bar span { height: 100%; }
</style>
</head>
<body>
  <article class="flyer">
    <svg class="header-band" viewBox="0 0 504 91" preserveAspectRatio="none" aria-hidden="true">
      <polygon points="142,0 504,0 504,91 185,91" fill="#0d4f9c"/>
    </svg>
    <div class="brand">
      <span class="brand-dot"></span>
      <div class="brand-name">CORVANE PROJECT<br>SERVICES</div>
    </div>

    <div class="hero" role="img" aria-label="Photo of colleagues reviewing printed charts and reports at a bright office table">
      <div class="hero-label">Corvane Project Services Ltd.</div>
    </div>

    <div class="director">
      <div class="director-name"><span class="first">Derek</span> Halloran</div>
      <div class="director-role">(Managing Director)</div>
      <ul class="contacts">
        <li>info@corvaneservices.ie <svg viewBox="0 0 8 8"><rect width="8" height="8" fill="#fff"/><path d="M1 2h6v4H1z M1 2l3 2 3-2" fill="none" stroke="#0d4f9c" stroke-width=".7"/></svg></li>
        <li>www.corvaneservices.ie <svg viewBox="0 0 8 8"><rect width="8" height="8" fill="#fff"/><circle cx="4" cy="4" r="2.5" fill="none" stroke="#0d4f9c" stroke-width=".7"/></svg></li>
        <li>+353 (0)87 555 0142 <svg viewBox="0 0 8 8"><rect width="8" height="8" fill="#fff"/><path d="M2 1.5l1 .3.3 1.3-.6.5a4 4 0 0 0 2 2l.5-.6 1.3.3.3 1C6 6.8 4.5 7 2.6 5.2 1 3.5 1.2 2 2 1.5z" fill="#0d4f9c"/></svg></li>
      </ul>
    </div>

    <div class="intro">
      <p>Corvane Project Services Ltd. is a leading project control consultancy based in Co Cork Ireland.<br>
      For over 20 years we have been helping our clients to deliver complex projects and programs<br>
      throughout mainland Europe.</p>
      <p>We are passionate about empower organisations to achieve their objectives, on time and on budget.</p>
      <p>We are continually innovating, evolving and learning, utilize the latest industry tools and techniques to<br>deliver real value to our clients.</p>
      <p>Our goal is to make successful project delivery more achievable and repeatable.</p>
    </div>

    <h2 class="services-title">Core Services</h2>
    <div class="services-rule"></div>
    <div class="services">
      <section class="service plan">
        <h3>Planning and Scheduling</h3>
        <ul>
          <li>Tender Planning</li>
          <li>Interactive Planning / Pull Planning</li>
          <li>EPCMV Planning &amp; Scheduling</li>
          <li>Schedule Earned Value Management</li>
          <li>Independent Schedule Quality Assessment</li>
          <li>Schedule Risk Analysis (Monte Carlo)</li>
          <li>Training</li>
        </ul>
      </section>
      <section class="service risk">
        <h3>Management of Risk</h3>
        <ul>
          <li>Risk Management Policies &amp; Procedures</li>
          <li>Risk Management Strategy</li>
          <li>Risk Registers</li>
          <li>Risk Improvement Planning</li>
          <li>Risk Response and Communication</li>
          <li>Risk Management Training</li>
        </ul>
      </section>
      <section class="service cost">
        <h3>Cost Control</h3>
        <ul>
          <li>Estimating &amp; Forecasting</li>
          <li>Earned Value Analysis</li>
          <li>Progress Reporting</li>
          <li>Cost Risk Analysis</li>
        </ul>
      </section>
    </div>

    <div class="tools">
      <span class="tool">Stratavera</span>
      <span class="tool"><i></i>Planwell</span>
      <span class="tool">Ostra Plan</span>
      <span class="tool">Waypoint Pro</span>
      <span class="tool">Kelvex</span>
      <span class="tool">Tallyo</span>
      <span class="tool">Riskora</span>
    </div>
    <div class="footer-bar">
      <span style="width:127px;background:var(--navy)"></span>
      <span style="width:210px;background:var(--sky)"></span>
      <span style="width:144px;background:var(--navy)"></span>
    </div>
  </article>
</body>
</html>
```